Meridale Legal Letterhead for Law firm must be modern and use the logo I uploaded.

Hello I want a clean modern professional letterhead for my law firm Meridale Legal. A logo has already been created and all files have been uploaded. The information for the firm can be given through message. Please use the logo that has already been created. Please also use the color scheme of that logo. (blue and white).

Target Market(s)

General Public

Industry/Entity Type

Law Firm

Colors

Designer to choose colors to be used in the design.

Requirements
Must have
• This must be a modern professional letterhead
Nice to have
• My logo that is included in file form
Should not have
• Should not have logo that is not the one I uploaded.

```html
<!DOCTYPE html>
<html lang="en">
<head>
<meta charset="utf-8">
<title>Meridale Legal Letterhead</title>
<link href="https://fonts.googleapis.com/css2?family=Montserrat:wght@600&family=Roboto:wght@400&display=swap" rel="stylesheet">
<style>
  :root {
    --backdrop: #dcdcdc;
    --paper: #ffffff;
    --navy: #2c3166;
    --rule: #6b6f9a;
    --ink: #555760;
  }
  * { margin: 0; padding: 0; box-sizing: border-box; }
  html, body {
    width: 1189px; height: 1200px; overflow: hidden;
    background: var(--backdrop);
  }
  .letterhead {
    position: absolute;
    left: 191px; top: 30px;
    width: 806px; height: 1140px;
    background: var(--paper);
  }
  .brand {
    position: absolute;
    left: 68px; top: 56px;
    display: flex; flex-direction: column; align-items: center;
  }
  .brand-mark {
    width: 48px; height: 48px;
    border-radius: 50%;
    background: var(--navy);
    margin-bottom: 24px;
  }
  .firm-name {
    font-family: "Montserrat", sans-serif;
    font-weight: 600;
    font-size: 13px;
    line-height: 16px;
    letter-spacing: 5px;
    margin-right: -5px;
    color: var(--navy);
    text-transform: uppercase;
    white-space: nowrap;
  }
  .header-rule {
    position: absolute;
    left: 68px; top: 151px;
    width: 670px; height: 1px;
    background: var(--rule);
  }
  .contact-list {
    position: absolute;
    left: 598px; top: 60px;
    list-style: none;
    font-family: "Roboto", sans-serif;
    font-size: 12.5px;
    line-height: 15.5px;
    color: var(--ink);
  }
  .contact-item {
    display: flex; align-items: flex-start;
  }
  .contact-item.address { margin-bottom: 6px; }
  .contact-icon {
    width: 10px; height: 10px;
    margin-right: 8px; margin-top: 3px;
    flex: none;
    fill: var(--navy);
  }
  .footer-band {
    position: absolute;
    left: 0; bottom: 0;
    width: 100%; height: 14px;
    background: var(--navy);
  }
</style>
</head>
<body>
  <main class="letterhead">
    <div class="brand">
      <div class="brand-mark"></div>
      <div class="firm-name">Meridale Legal</div>
    </div>
    <div class="header-rule"></div>

    <ul class="contact-list">
      <li class="contact-item address">
        <svg class="contact-icon" viewBox="0 0 10 10"><path d="M5 0a3.6 3.6 0 0 0-3.6 3.6C1.4 6.3 5 10 5 10s3.6-3.7 3.6-6.4A3.6 3.6 0 0 0 5 0zm0 5a1.4 1.4 0 1 1 0-2.8A1.4 1.4 0 0 1 5 5z"/></svg>
        <span>Your address, city<br>state, ZIP 0000</span>
      </li>
      <li class="contact-item">
        <svg class="contact-icon" viewBox="0 0 10 10"><path d="M2.2 0.6 3.8 2.4 3 3.6c.6 1.4 1.8 2.6 3.2 3.2l1.2-.8 1.8 1.6-1 1.6C4.4 9.2.6 5.4.6 1.6z"/></svg>
        <span>123-456-2100</span>
      </li>
      <li class="contact-item">
        <svg class="contact-icon" viewBox="0 0 10 10"><path d="M0 2h10v6H0z M0.6 2.4 5 5.6 9.4 2.4" stroke="#fff" stroke-width="0.8"/></svg>
        <span>youremail@mailbox.com</span>
      </li>
      <li class="contact-item">
        <svg class="contact-icon" viewBox="0 0 10 10"><circle cx="5" cy="5" r="5"/><path d="M0 5h10M5 0c-2 2.5-2 7.5 0 10M5 0c2 2.5 2 7.5 0 10" stroke="#fff" stroke-width="0.7" fill="none"/></svg>
        <span>www.yourwebsite.com</span>
      </li>
    </ul>

    <div class="footer-band"></div>
  </main>
</body>
</html>
```